Telmoro Business Card

I already have the conplay logo. I need to develop a professional business card layout

Target Market(s)

Business

Industry/Entity Type

Business

Contact Information for Business Card

Company Name: Telmoro Limited

Font styles to use
Sans Serif

Colors

Designer to choose colors to be used in the design.

Requirements
Must have
• Use current logo
• Need two card size options:
• Small Card: 70mm x 28mm (Landscape)
• Square Card: 65mm x 65mm
Nice to have
• I will need 8-10 files for each name, number and email address (details to follow)

```html
<!DOCTYPE html>
<html lang="en">
<head>
<meta charset="utf-8">
<title>Telmoro Limited – Business Card</title>
<link rel="stylesheet" href="https://fonts.googleapis.com/css2?family=Roboto+Condensed:wght@400;700&display=swap">
<style>
  :root {
    --backdrop: #e4e5e7;
    --card: #ffffff;
    --ink: #1f1f7f;
    --footer-top: #1f1f7f;
    --footer-bottom: #2a6fb0;
  }
  html, body {
    margin: 0;
    padding: 0;
    width: 1200px;
    height: 1000px;
    overflow: hidden;
    background: var(--backdrop);
    font-family: "Roboto Condensed", "Arial Narrow", sans-serif;
  }
  .canvas {
    position: relative;
    width: 1200px;
    height: 1000px;
  }
  .card {
    position: absolute;
    left: 463px;
    top: 143px;
    width: 272px;
    height: 681px;
    background: var(--card);
    color: var(--ink);
    overflow: hidden;
  }
  .wordmark {
    position: absolute;
    left: 213px;
    top: 223px;
    transform: translate(-50%, -50%) rotate(-90deg);
    font-weight: 700;
    font-size: 84px;
    line-height: 1;
    letter-spacing: 6px;
    white-space: nowrap;
    color: var(--ink);
    margin: 0;
  }
  .contact {
    position: absolute;
    left: 20px;
    top: 324px;
    margin: 0;
    font-weight: 400;
  }
  .contact p { margin: 0; }
  .name { font-size: 21px; line-height: 26px; }
  .role { font-size: 13px; line-height: 18px; }
  .lines { font-size: 17px; line-height: 23px; }
  .direct { margin-top: 50px !important; }
  .company { margin-top: 23px !important; }
  .footer-band {
    position: absolute;
    left: 0;
    top: 569px;
    width: 272px;
    height: 112px;
    background: linear-gradient(180deg, var(--footer-top), var(--footer-bottom));
  }
</style>
</head>
<body>
<div class="canvas">
  <article class="card">
    <h1 class="wordmark">TELMORO</h1>

    <div class="contact">
      <p class="name">Mara Quinlan</p>
      <p class="role">CEO</p>
      <p class="lines direct">2468 135 790<br>mara@telmoro.com</p>
      <p class="lines company">Telmoro Limited<br>www.telmoro.com<br>48 Harbour Rd Telmoro 5120</p>
    </div>

    <div class="footer-band" role="img" aria-label="Decorative colour band along the foot of the card"></div>
  </article>
</div>
</body>
</html>
```